Custom Beer Labelling Company Needs a Flyer

We need a flyer designed to promote Hopwrapz, a new company in Sydney that helps home brewers create their own small batch beer labels. Main purpose of the flyer is to increase awareness of the service we offer and drive traffic to the Hopwrapz shopify site - www.hopwrapz-example.com.au.
Our value proposition is about being easy (less than 5 minutes), affordable (full set of labels from only $12) with good quality (water resistant synthetic labels that remove cleanly).
The flyer should suit A4 printing and will preferably include screenshot of the "Create your Label" tool on the site, and/or examples of our label templates. It may also include other information from our site such eg from the "About Us" or About Our Labels" pages.

Target Market(s)

Home brewers, mostly males aged 20-50

Industry/Entity Type

It Company

Colors
ec1f27
fee3d4
f9ba93
f68d4e
f37122
f78f20
faa54b
fbc994
ffffff

Requirements
Must have
• Drive customers to www.hopwrapz-example.com as call to action
Nice to have
• screenshot(s) and examples of labels

```html
<!DOCTYPE html>
<html lang="en">
<head>
<meta charset="utf-8">
<title>Hopwrapz – Small Batch Beer Labels Flyer</title>
<link href="https://fonts.googleapis.com/css2?family=Montserrat:ital,wght@0,500;0,700;0,800;1,600;1,700;1,800&family=Nunito+Sans:wght@400;700&display=swap" rel="stylesheet">
<style>
  :root {
    --red: #d1232a;
    --red-deep: #c0212a;
    --orange: #f37122;
    --orange-bright: #f78f20;
    --amber: #faa54b;
    --yellow: #f6c01c;
    --brown: #5a3a22;
    --ink: #1f1f1f;
    --sky-top: #dbe3ea;
    --sky-mid: #f2f5f7;
    --sky-low: #cfdae4;
    --white: #ffffff;
  }
  * { margin: 0; padding: 0; box-sizing: border-box; }
  html, body { width: 957px; height: 1200px; overflow: hidden; }
  body { font-family: "Nunito Sans", Arial, sans-serif; color: var(--ink); }

  .flyer {
    position: relative;
    width: 957px;
    height: 1200px;
    overflow: hidden;
    background: linear-gradient(180deg, var(--sky-top) 0%, var(--sky-mid) 38%, var(--sky-mid) 55%, var(--sky-low) 100%);
  }

  .brand {
    position: absolute;
    left: 42px;
    top: 52px;
    display: flex;
    align-items: center;
    gap: 10px;
    font-family: "Montserrat", Arial, sans-serif;
    font-weight: 700;
    font-size: 38px;
    color: var(--brown);
  }
  .brand-mark {
    width: 40px; height: 40px;
    background: var(--orange);
  }

  .hero-band { position: absolute; left: 0; top: 0; width: 957px; height: 360px; }
  .hero-band text { font-family: "Montserrat", Arial, sans-serif; fill: var(--white); }
  .headline { font-weight: 800; font-size: 62px; }
  .subline { font-weight: 500; font-size: 40px; }
  .band-url { font-weight: 700; font-size: 25px; }

  .value-prop {
    position: absolute;
    left: 0; right: 0;
    top: 366px;
    text-align: center;
    font-size: 30px;
    line-height: 39px;
    color: var(--ink);
  }

  .product-visual {
    position: absolute;
    left: 57px; top: 481px;
    width: 818px; height: 410px;
    border-radius: 10px;
    background:
      radial-gradient(ellipse at 80% 50%, #6b2a1e 0%, #4a2216 22%, transparent 40%),
      linear-gradient(180deg, #3a3a3c 0%, #7d2a32 30%, #b43a45 55%, #e6e7e9 80%, #b9bcc0 100%);
  }

  .details {
    position: absolute;
    left: 0; right: 0;
    top: 926px;
    text-align: center;
    font-size: 12.5px;
    line-height: 16.5px;
    color: #2a2a2a;
  }
  .details strong { font-weight: 700; }

  .footer-shapes { position: absolute; left: 0; top: 980px; width: 957px; height: 220px; }

  .tagline {
    position: absolute;
    left: 37px; top: 1068px;
    font-family: "Montserrat", Arial, sans-serif;
    font-style: italic;
    color: var(--white);
    line-height: 1;
  }
  .tagline .big { display: block; font-weight: 800; font-size: 34px; margin-bottom: 2px; }
  .tagline .small { display: block; font-weight: 600; font-size: 21px; margin-top: 4px; }

  .cta {
    position: absolute;
    right: 51px; top: 1052px;
    text-align: right;
    font-family: "Montserrat", Arial, sans-serif;
    font-style: italic;
  }
  .cta-line { font-weight: 600; font-size: 21px; line-height: 29px; color: var(--ink); }
  .cta-url { margin-top: 14px; font-weight: 800; font-size: 19px; color: var(--orange-bright); }
</style>
</head>
<body>
<main class="flyer">

  <svg class="hero-band" viewBox="0 0 957 360">
    <defs>
      <linearGradient id="bandGradient" x1="0" y1="0" x2="1" y2="0">
        <stop offset="0" stop-color="#c8202a"/>
        <stop offset="0.35" stop-color="#d8352a"/>
        <stop offset="0.7" stop-color="#f37122"/>
        <stop offset="1" stop-color="#f7bd1e"/>
      </linearGradient>
      <linearGradient id="urlGradient" x1="0" y1="0" x2="1" y2="0">
        <stop offset="0" stop-color="#f6c01c"/>
        <stop offset="0.45" stop-color="#f37122"/>
        <stop offset="1" stop-color="#c8202a"/>
      </linearGradient>
    </defs>
    <polygon points="0,168 957,53 957,204 0,320" fill="url(#bandGradient)"/>
    <polygon points="262,266 822,196 808,267 246,336" fill="url(#urlGradient)"/>
    <g transform="rotate(-8.6 121 214)">
      <text class="headline" x="121" y="214">EASY &amp; AFFORDABLE</text>
    </g>
    <g transform="rotate(-8.6 124 259)">
      <text class="subline" x="124" y="259">SMALL BATCH BEER LABELS AT</text>
    </g>
    <g transform="rotate(-7.2 290 306)">
      <text class="band-url" x="290" y="306">WWW.HOPWRAPZ-EXAMPLE.COM.AU</text>
    </g>
  </svg>

  <div class="brand">
    <span class="brand-mark"></span>
    <span class="brand-name">Hopwrapz</span>
  </div>

  <p class="value-prop">Less than five minutes and from just $12<br>for a full set of custom printed labels.</p>

  <div class="product-visual" role="img" aria-label="Laptop showing the Create Your Label tool beside three brown beer bottles wearing red custom labels"></div>

  <p class="details">
    Just fill in template with details of your brew, and select from our range of designs, colours, icons and bottle size.<br>
    We print your labels in <strong>high quality LED</strong> on A4 sheets of die cut, <strong>self-adhesive</strong> labels. Our synthetic labels are<br>
    <strong>water resistant</strong> and remove cleanly from your empties without tearing and without leftover glue crud.
  </p>

  <svg class="footer-shapes" viewBox="0 0 957 220" aria-hidden="true">
    <polygon points="239,78 957,25 957,220 0,220" fill="var(--white)"/>
    <polygon points="0,3 628,220 0,220" fill="var(--orange-bright)"/>
  </svg>

  <p class="tagline">
    <span class="big">TAKE YOUR</span>
    <span class="big">HOMEBREW</span>
    <span class="small">TO ANOTHER LEVEL</span>
  </p>

  <div class="cta">
    <p class="cta-line">Try a set of Hopwrapz next time</p>
    <p class="cta-line">you lay down a batch.</p>
    <p class="cta-url">www.hopwrapz-example.com.au</p>
  </div>

</main>
</body>
</html>
```